Lotvantage.com Webpage Design

Design Brief for lotvantage.com (Copy of Brief also in attached Word file)

Name of Website- lotvantage.com (existing logo and look & feel of website to be changed)

Logo - Finalised. The logo files are attached with the brief as “logo.jpeg”. The “Blue- Grey” version of the logo is for use on lighter backgrounds and the “Orange-White” version of the logo is for use on darker backgrounds. (A full Black version of the logo is also attached). Both versions may be used in different parts of the website. All attached files are in .png format.
Status - The website in functional and is undergoing user trials. However, we want to improve the look & feel of the website so at it seems
a. cotemporary,
b. Easy to Navigate
c. professional and
d. Vibrant.

Please visit ‘lotvantage.com’ to check out the website and its functionalities – please use it only as a reference for the features & functions to be provided, however the designer should use a ‘Free Hand’ in designing the composition of various parts of the webpage without getting too influenced by the existing design

Objective of the Website ‘lotvantage.com –
a. It is a portal focussed on listing of ‘Retail’ specific real-estate properties by developers, owners and realty brokers. The properties shall listed under the following four categories-
i. Retail Malls
ii. Shopping Complexes
iii. High-street shops
iv. Retail Warehouses
*refer lotvantage.com for better clarity

b. The abovementioned properties shall be listed either for ‘Sale’ or ‘rent\lease’ or both

c. Users shall visit the site in case they wish to acquire a retail \ shop space either on ‘sale’ or ‘rent’. These Users would be able to specify the ‘Search Criteria’ through the tool-bars provided on the website – the ‘Search Criteria’ shall comprise of ‘Type of space category’, ‘City’, ‘Locality’, transaction type ie ‘Rent \ Sale’ and ‘Area Range’

d. The main revenue model for the website shall be listing fee ( or advertising charges ) payable by those listing their properties on the website.

Three Main Pages of Website (lotvantage.com) that need to be designed -
a. Main Home Page (visit the web link - http://lotvantage.com/ ) - The main home page has the “Search Toolbar” for specifying of Search Criteria by the User. It shall also have the following features & functions-
i. Main Advertising Banner
ii. Featured Projects
iii. New Launches
iv. Toolbar with buttons – ‘Advertise with Us’, ‘Listings Alert’, ‘Lot Mavens’, ‘Advertiser Login’

b. Property Listings Page (visit the web link - http://lotvantage.com/gurgaon-in-india ) - The List of property options that match the Criteria specified by the ‘User’ get displayed on this page.

c. Property Detail Page - When the ‘User’ clicks on the “More….” Button on the ‘Property Listings Page’ (given in point b. above) the web page with the details of the property opens. (For Example – visit the web link - http://lotvantage.com/brevo-Shopping-Complex-brevo-quadrel-gurgaon-636 )

Note:- Please refer to attached ‘Shopping’ related images the designer may use them on the website to provide a look & feel of retail if required – either separately or rotate in a single window

Target Market(s)

Retailers & Investors looking for retail space, Real Estate Brokers, Developers

Industry/Entity Type

Advertising

Number of Pages Required

3 page

Requirements
Must have
• Refer to existing site lotvantage.com -- all the existing functionalities are a must have.
Nice to have
• The Designer may use the retail related images on the website if required for making it more vibrant. Refer attached images Shopping(1-6).jpg

```html
<!DOCTYPE html>
<html lang="en">
<head>
<meta charset="utf-8">
<title>Lotvantage.com – Find Perfect Place for Your Retail Store</title>
<link rel="stylesheet" href="https://fonts.googleapis.com/css2?family=Open+Sans:wght@400;600;700;800&display=swap">
<style>
:root{
  --orange:#f0a63b;
  --blue:#0a9cf0;
  --blue-dark:#0684cc;
  --nav-blue:#1a95e0;
  --ink:#222;
  --grey:#555;
  --muted:#666;
  --line:#cfcfcf;
  --white:#fff;
}
*{box-sizing:border-box;margin:0;padding:0}
html,body{width:1200px;height:846px;overflow:hidden;background:var(--white);font-family:"Open Sans",Arial,sans-serif;color:var(--ink)}
.page{position:relative;width:1200px;height:846px;overflow:hidden}

/* city strip */
.city-strip{position:absolute;left:0;top:0;width:1200px;height:21px;background:var(--orange);display:flex;justify-content:flex-end;padding-right:129px;align-items:center}
.city-strip a{color:var(--white);font-size:11.5px;font-weight:600;text-decoration:none;padding:0 5px;border-left:1px solid rgba(255,255,255,.85);line-height:12px}
.city-strip a:first-child{border-left:none}

/* header */
.site-header{position:absolute;left:0;top:21px;width:1200px;height:94px;background:var(--white)}
.brand{position:absolute;left:130px;top:30px;display:flex;align-items:center;gap:8px;text-decoration:none}
.brand-dot{width:30px;height:30px;border-radius:50%;background:var(--blue)}
.brand-name{font-size:26px;font-weight:700;color:#3f4a55;letter-spacing:-.5px}
.main-nav{position:absolute;top:35px;left:0;width:1200px}
.nav-item{position:absolute;text-decoration:none;text-align:center;color:var(--ink);font-size:14px;line-height:16px}
.nav-item small{display:block;font-size:11px;color:var(--muted);margin-top:2px}
.nav-item.is-active{color:var(--nav-blue)}
.nav-home{left:479px}
.nav-advertise{left:563px}
.nav-mavens{left:719px}
.nav-alert{left:840px}
.account{position:absolute;left:939px;top:9px;width:151px}
.account-link{display:block;font-size:11px;line-height:15px;color:var(--nav-blue);text-decoration:none;font-weight:600}
.login-btn{display:block;margin:2px 0 3px;height:35px;background:var(--blue);color:var(--white);border-radius:3px;font-size:15px;font-weight:600;text-align:center;line-height:35px;text-decoration:none;border-bottom:2px solid var(--blue-dark)}

/* hero */
.hero{position:absolute;left:0;top:115px;width:1200px;height:601px}
.hero-photo{position:absolute;inset:0;background:
  radial-gradient(ellipse at 30% 20%,rgba(230,200,140,.55),transparent 55%),
  radial-gradient(ellipse at 85% 35%,rgba(200,150,90,.45),transparent 50%),
  linear-gradient(180deg,#4a3a2c 0%,#3b2e24 45%,#2a221c 100%)}
.hero-title{position:absolute;left:128px;top:255px;color:var(--white);font-size:40px;font-weight:800;line-height:45px;letter-spacing:-.2px;text-shadow:2px 2px 0 #3a3a3a,0 0 6px rgba(0,0,0,.5)}

/* search panel */
.search-panel{position:absolute;left:744px;top:25px;width:356px;height:552px;background:var(--white);border-radius:3px;padding:20px 25px 0}
.search-title{font-size:24px;font-weight:400;color:var(--ink);line-height:30px;position:relative}
.search-title span{color:var(--orange);font-weight:600}
.search-title::after{content:"";position:absolute;left:0;top:32px;width:22px;height:3px;background:var(--orange)}
.field-label{display:block;font-size:14px;line-height:20px;font-weight:600;color:#333;margin-top:13px}
.field-label.first{margin-top:16px}
.field-label a{color:var(--nav-blue);text-decoration:underline}
.formats{display:grid;grid-template-columns:155px 150px;row-gap:6px;margin-top:8px}
.radio{display:flex;align-items:center;gap:8px;font-size:14px;line-height:20px;color:var(--grey)}
.radio i{width:14px;height:14px;border:1px solid #aaa;border-radius:50%;display:inline-block}
.select{position:relative;width:300px;margin-top:9px;height:35px;border:1px solid var(--line);border-radius:3px;font-size:14px;color:var(--grey);line-height:33px;padding-left:13px}
.select::before{content:"";position:absolute;right:37px;top:0;bottom:0;border-left:1px solid var(--line)}
.select svg{position:absolute;right:14px;top:14px}
.input{width:300px;margin-top:9px;height:35px;border:1px solid var(--line);border-radius:3px;font-size:14px;color:var(--grey);line-height:33px;padding-left:13px}
.search-btn{display:block;width:300px;height:53px;margin-top:21px;background:var(--blue);color:var(--white);font-size:17px;font-weight:700;border-radius:3px;border-bottom:3px solid var(--blue-dark);text-align:center;line-height:51px;letter-spacing:.3px}

/* category tiles */
.categories{position:absolute;left:130px;top:743px;display:flex;gap:20px}
.category{width:220px;height:83px;background:var(--orange);border-radius:2px;text-align:center;text-decoration:none;padding-top:15px}
.category h3{font-size:18px;font-weight:600;color:#2b2b2b;line-height:22px}
.category p{font-size:14px;color:#333;margin-top:6px}
</style>
</head>
<body>
<div class="page">
  <nav class="city-strip" aria-label="Cities">
    <a href="#">Bangalore</a><a href="#">Chennai</a><a href="#">Greater Noida</a><a href="#">Gurgaon</a><a href="#">Hyderabad</a><a href="#">Jaipur</a><a href="#">Khanna</a><a href="#">Kolkatta</a><a href="#">Mumbai</a><a href="#">Noida</a><a href="#">Pune</a><a href="#">Surat</a>
  </nav>

  <header class="site-header">
    <a class="brand" href="#"><span class="brand-dot"></span><span class="brand-name">Lotvantage.com</span></a>
    <nav class="main-nav">
      <a class="nav-item nav-home is-active" href="#">Home</a>
      <a class="nav-item nav-advertise" href="#">Advertise with us<small>Standard listing - FREE</small></a>
      <a class="nav-item nav-mavens" href="#">Lot Mavens<small>Shop Search Services</small></a>
      <a class="nav-item nav-alert" href="#">Listing Alert</a>
    </nav>
    <div class="account">
      <a class="account-link" href="#">List Your Property Here</a>
      <a class="login-btn" href="#">Advertiser Login</a>
      <a class="account-link" href="#">New Advertiser - Register</a>
    </div>
  </header>

  <section class="hero">
    <div class="hero-photo" role="img" aria-label="Photo of a smiling family walking through a lit shopping mall courtyard in the evening"></div>
    <h1 class="hero-title">Find Perfect Place for<br>Your Retail Store</h1>

    <form class="search-panel">
      <h2 class="search-title">Find your <span>retail space</span></h2>
      <span class="field-label first">Select <a href="#">Retail Fromat</a>:</span>
      <div class="formats">
        <span class="radio"><i></i>Retail Malls</span>
        <span class="radio"><i></i>Shopping Complex</span>
        <span class="radio"><i></i>High Street Shops</span>
        <span class="radio"><i></i>Retail Warehouses</span>
      </div>
      <span class="field-label">Sale Or Rent Or Both:</span>
      <div class="select">Both<svg width="10" height="6" viewBox="0 0 10 6"><path d="M0 0h10L5 6z" fill="#555"/></svg></div>
      <span class="field-label">Select City:</span>
      <div class="select">Select<svg width="10" height="6" viewBox="0 0 10 6"><path d="M0 0h10L5 6z" fill="#555"/></svg></div>
      <span class="field-label">Select Locality/Micro-Market.</span>
      <div class="select">Select<svg width="10" height="6" viewBox="0 0 10 6"><path d="M0 0h10L5 6z" fill="#555"/></svg></div>
      <span class="field-label">Enter Keywords:</span>
      <div class="input">Name of the Project, Developer etc</div>
      <span class="search-btn">SEARCH</span>
    </form>
  </section>

  <section class="categories">
    <a class="category" href="#"><h3>Retail Malls</h3><p>Centrally Air-Conditioned</p></a>
    <a class="category" href="#"><h3>Shopping Complex</h3><p>Non Air-Conditioned Building</p></a>
    <a class="category" href="#"><h3>High Street Shops</h3><p>Road Facing Retail</p></a>
    <a class="category" href="#"><h3>Retail Warehouses</h3><p>Back-end Ratail Storage</p></a>
  </section>
</div>
</body>
</html>
```